New tech executive consulting company needs professionally branded document templates

We are a new business selling fractional board advisory and go-to-market consulting services into the Technology space. Partwise Helm are experts in providing high-quality executive-level leaders on a part-time basis to tech companies in need of their expertise. We work closely with clients to understand their business needs, challenges, and goals, and provides customised solutions to help them succeed. Due to our audience we need the design to have a high quality, executive look and feel.

Our first website is live and can be found at partwisehelm.tech. We also already have a logo which I've uploaded. Our brand is clean and uses orange to give it colour and an identity that stands out.

We need some document master templates created so we can create our own presentations (Google Slides & Powerpoint), PDF documents, and Word templates, and ideally also a LinkedIn banner.

```html
<!DOCTYPE html>
<html lang="en">
<head>
<meta charset="utf-8">
<title>Partwise Helm – Presentation Templates</title>
<link rel="stylesheet" href="https://fonts.googleapis.com/css2?family=Bebas+Neue&family=Montserrat:wght@400;500;600;700&display=swap">
<style>
:root{
  --canvas:#d1d2d4;
  --navy:#293241;
  --orange:#ee874d;
  --grey-band:#e9e7e5;
  --white:#ffffff;
  --ink:#2a2a2a;
  --muted:#8c8c8c;
  --photo-light:#c9d3d6;
  --photo-dark:#4a5260;
}
*{margin:0;padding:0;box-sizing:border-box}
html,body{width:777px;height:1200px;overflow:hidden;background:var(--canvas)}
body{position:relative;font-family:'Montserrat',sans-serif;color:var(--ink)}
.slide{position:absolute;width:277px;height:173px;background:var(--white);overflow:hidden}
.col-l{left:88px}.col-r{left:412px}
.row1{top:105px}.row2{top:308px}.row3{top:508px}.row4{top:707px}.row5{top:907px}
.display{font-family:'Bebas Neue',sans-serif;line-height:.95;letter-spacing:.2px}
.brand{position:absolute;font-family:'Montserrat',sans-serif;font-weight:700;color:var(--navy);letter-spacing:.6px;white-space:nowrap}
.brand.on-dark{color:var(--white)}
.brand-lg{font-size:8.5px;left:15px;top:22px}
.brand-sm{font-size:4.6px;left:8px;bottom:12px}
.page-no{position:absolute;right:8px;bottom:8px;font-size:4px;color:var(--navy);border-left:.6px solid var(--orange);padding-left:2px}
.copyright-bar{position:absolute;left:0;bottom:0;width:100%;height:13px;background:var(--grey-band);font-size:3.4px;color:var(--muted);text-align:center;line-height:13px}
.photo{position:absolute}
.cover-title{position:absolute;left:15px;top:62px;font-size:22px}
.cover-title .l1{color:var(--navy)}
.cover-title .l2{color:var(--orange)}
.on-dark .l1{color:var(--white)}
.cover-sub{position:absolute;left:15px;top:104px;font-size:6px;color:var(--navy)}
.on-dark .cover-sub,.cover-sub.light{color:var(--white)}
.pill{position:absolute;left:15px;top:119px;background:var(--orange);color:var(--white);font-size:5.4px;padding:2px 6px;border-radius:6px}
.head-band{position:absolute;left:0;top:0;width:100%;height:43px;background:var(--grey-band)}
.head-band.orange{background:var(--orange)}
.head-title{position:absolute;left:8px;top:15px;font-size:13px;color:var(--orange)}
.head-band.orange .head-title{color:var(--white);left:11px}
.body-copy{position:absolute;font-size:3.9px;line-height:1.95;text-align:justify;color:var(--ink)}
.navy-box{position:absolute;background:var(--navy);color:var(--white)}
.mini-title{font-size:5.4px;font-weight:500}
.mini-copy{font-size:2.9px;line-height:1.3}
.feature{position:absolute;width:125px;height:34px}
.feature .icon{position:absolute;left:0;top:5px;width:19px;height:19px;border-radius:50%;background:var(--orange)}
.feature .rule{position:absolute;left:23px;top:0;width:.5px;height:30px;background:var(--white)}
.feature .text{position:absolute;left:28px;top:3px;width:96px;color:var(--white)}
.orange-t{color:var(--orange);font-size:5.2px;font-weight:500}
.data-table{position:absolute;left:15px;top:52px;width:248px;border-collapse:collapse;font-size:3.3px}
.data-table th{background:var(--navy);color:var(--white);font-weight:500;height:12px;text-align:center}
.data-table th:first-child{text-align:left;padding-left:2px}
.data-table td{height:11.2px;border-bottom:.4px solid #bbb;text-align:center}
.data-table td:first-child{text-align:left;padding-left:2px}
.data-table .hl{background:var(--orange)}
.col-frame{position:absolute;left:91px;top:49px;width:43px;height:97px;border:.8px solid var(--orange);border-radius:4px}
.card{position:absolute;top:74px;width:76px}
.card .ph{height:36px}
.card .orange-t{text-align:center;margin-top:4px}
.card .bullet{font-size:3.1px;margin-top:5px;padding-left:9px;position:relative;line-height:1.2}
.card .bullet::before{content:"";position:absolute;left:2px;top:1px;width:1.8px;height:1.8px;border-radius:50%;background:var(--orange)}
.person{position:absolute;top:63px;width:44px;text-align:center}
.person .avatar{width:28px;height:28px;margin:0 auto;border-radius:50%;background:var(--orange);border:2px solid var(--white)}
.person .name{font-size:5.2px;font-weight:500;margin-top:5px}
.person .mini-copy{font-size:2.7px;text-align:justify;margin-top:1px}
.contact{position:absolute;left:24px;top:128px;font-size:5.6px;color:var(--white);line-height:1.75}
</style>
</head>
<body>

<!-- Cover, light -->
<section class="slide col-l row1">
  <div class="photo" role="img" aria-label="Photo of a smiling executive presenting in a bright meeting room" style="left:90px;top:0;width:187px;height:160px;background:linear-gradient(90deg,var(--white) 0%,#e3e9ea 30%,var(--photo-light) 65%,#6f7f86 100%)"></div>
  <div class="brand brand-lg">PARTWISE HELM</div>
  <div class="cover-title display"><div class="l1">PRESENTATION</div><div class="l2">TITLE GOESHERE</div></div>
  <div class="cover-sub">Subtitle of Presentation Goes Here</div>
  <div class="pill">www.partwisehelm.tech</div>
  <div class="copyright-bar">©2023 Partwise Helm. All Copyright Reserved</div>
</section>

<!-- Cover, dark -->
<section class="slide col-r row1 on-dark" style="background:var(--navy)">
  <div class="photo" role="img" aria-label="Photo of a smiling executive presenting in a meeting room" style="left:90px;top:0;width:187px;height:160px;background:linear-gradient(90deg,var(--navy) 0%,#3b4452 35%,var(--photo-dark) 70%,#7a8288 100%)"></div>
  <div class="brand brand-lg on-dark">PARTWISE HELM</div>
  <div class="cover-title display"><div class="l1">PRESENTATION</div><div class="l2">TITLE GOESHERE</div></div>
  <div class="cover-sub">Subtitle of Presentation Goes Here</div>
  <div class="pill">www.partwisehelm.tech</div>
  <div class="copyright-bar">©2023 Partwise Helm. All Copyright Reserved</div>
</section>

<!-- Disclaimer -->
<section class="slide col-l row2">
  <div class="head-band"><div class="head-title display">DISCLAIMER</div></div>
  <p class="body-copy" style="left:8px;top:49px;width:261px">Lorem ipsum dolor sit amet, consectetuer adipiscing elit, sed diam nonummy nibh euismod tincidunt ut laoreet dolore magna aliquam erat volutpat. Ut wisi enim ad minim veniam, quis nostrud exerci tation ullamcorper suscipit lobortis nisl ut aliquip ex ea commodo consequat. Duis autem vel eum iriure dolor in hendrerit in vulputate velit esse molestie consequat, vel illum dolore eu feugiat nulla facilisis at vero eros et accumsan et iusto odio dignissim qui blandit praesent luptatum zzril delenit augue duis dolore te feugait nulla facilisi.</p>
  <p class="body-copy" style="left:8px;top:96px;width:261px">Lorem ipsum dolor sit amet, cons ectetuer adipiscing elit, sed diam nonummy nibh euismod tincidunt ut laoreet dolore magna aliquam erat volutpat. Ut wisi enim ad minim veniam, quis nostrud exerci tation ullamcorper suscipit lobortis nisl ut aliquip ex ea commodo consequat.</p>
  <div class="brand brand-sm">PARTWISE HELM</div>
  <div class="page-no">01</div>
</section>

<!-- Why invest -->
<section class="slide col-r row2">
  <div class="head-band orange">
    <div class="photo" role="img" aria-label="Faded photo of a team meeting" style="right:0;top:0;width:110px;height:43px;background:linear-gradient(90deg,var(--orange),#c98a66 60%,#9a8378)"></div>
    <div class="head-title display">WHY WOULD YOU INVEST WITH US?</div>
  </div>
  <div class="photo" role="img" aria-label="Photo of an executive leading a meeting at an office table" style="left:13px;top:58px;width:97px;height:78px;background:linear-gradient(135deg,#b7c3c6,#6d7b80 60%,#3e4750)"></div>
  <div class="navy-box" style="left:110px;top:58px;width:155px;height:78px;padding:8px 6px">
    <div class="display" style="color:var(--orange);font-size:6.5px">YOU WANT:</div>
    <p class="mini-copy" style="font-size:3.2px;line-height:1.7;text-align:justify;margin-top:2px">Lorem ipsum dolor sit amet, consectetuer adipiscing elit, sed diam nonummy nibh euismod tincidunt ut laoreet dolore magna aliquam erat volutpat. Ut lobortis nisl ut aliquip ex ea commodo consequat. Duis autem vel eum iriure dolor hendrerit in vulputate velit</p>
    <p class="mini-copy" style="font-size:3.2px;line-height:1.7;text-align:justify;margin-top:4px">esse molestie consequat, vel illum dolore eu feugiat nulla facilisis at vero eros et accumsan et iusto odio dignissim qui blandit praesent luptatum zzril delenit augue duis dolore te feugait nulla facilisi.</p>
  </div>
  <div class="brand brand-sm">PARTWISE HELM</div>
  <div class="page-no">02</div>
</section>

<!-- Why not right -->
<section class="slide col-l row3">
  <div class="head-band orange">
    <div class="photo" role="img" aria-label="Faded photo of a team meeting" style="right:0;top:0;width:110px;height:43px;background:linear-gradient(90deg,var(--orange),#c98a66 60%,#9a8378)"></div>
    <div class="head-title display">WHY WE MAY NOT BE RIGHT FOR YOU</div>
  </div>
  <div class="navy-box" style="left:0;top:56px;width:277px;height:87px">
    <div class="feature" style="left:14px;top:10px"><div class="icon"></div><div class="rule"></div><div class="text"><div class="mini-title">Title Goes Here</div><p class="mini-copy">Lorem ipsum dolor sit amet, consectetuer adipiscing elit, sed diam nonummy nibh euismod tincidunt ut laoreet dolore magna aliquam erat volutpat. Ut wisi enim ad minim veniam, quis nostrud exerci tation ullamcorper suscipit lobortis nisl ut</p></div></div>
    <div class="feature" style="left:144px;top:10px"><div class="icon"></div><div class="rule"></div><div class="text"><div class="mini-title">Title Goes Here</div><p class="mini-copy">Lorem ipsum dolor sit amet, consectetuer adipiscing elit, sed diam nonummy nibh euismod tincidunt ut laoreet dolore magna aliquam erat volutpat. Ut wisi enim ad minim veniam, quis nostrud exerci tation ullamcorper suscipit lobortis nisl ut</p></div></div>
    <div class="feature" style="left:14px;top:49px"><div class="icon"></div><div class="rule"></div><div class="text"><div class="mini-title">Title Goes Here</div><p class="mini-copy">Lorem ipsum dolor sit amet, consectetuer adipiscing elit, sed diam nonummy nibh euismod tincidunt ut laoreet dolore magna aliquam erat volutpat. Ut wisi enim ad minim veniam, quis nostrud exerci tation ullamcorper suscipit lobortis nisl ut</p></div></div>
    <div class="feature" style="left:144px;top:49px"><div class="icon"></div><div class="rule"></div><div class="text"><div class="mini-title">Title Goes Here</div><p class="mini-copy">Lorem ipsum dolor sit amet, consectetuer adipiscing elit, sed diam nonummy nibh euismod tincidunt ut laoreet dolore magna aliquam erat volutpat. Ut wisi enim ad minim veniam, quis nostrud exerci tation ullamcorper suscipit lobortis nisl ut</p></div></div>
  </div>
  <div class="brand brand-sm">PARTWISE HELM</div>
  <div class="page-no">03</div>
</section>

<!-- Performance -->
<section class="slide col-r row3">
  <div class="head-band"><div class="head-title display">PERFORMANCE SINCE INCEPTION</div></div>
  <svg class="perf-chart" style="position:absolute;left:10px;top:62px" width="140" height="64" viewBox="0 0 140 64">
    <g stroke="#e2e2e2" stroke-width=".4">
      <line x1="4" y1="6" x2="134" y2="6"/><line x1="4" y1="13" x2="134" y2="13"/><line x1="4" y1="20" x2="134" y2="20"/>
      <line x1="4" y1="27" x2="134" y2="27"/><line x1="4" y1="34" x2="134" y2="34"/><line x1="4" y1="41" x2="134" y2="41"/>
      <line x1="4" y1="48" x2="134" y2="48"/>
      <line x1="25" y1="4" x2="25" y2="55"/><line x1="47" y1="4" x2="47" y2="55"/><line x1="68" y1="4" x2="68" y2="55"/>
      <line x1="90" y1="4" x2="90" y2="55"/><line x1="111" y1="4" x2="111" y2="55"/>
    </g>
    <line x1="4" y1="2" x2="4" y2="55" stroke="#999" stroke-width=".5"/>
    <line x1="4" y1="55" x2="136" y2="55" stroke="#999" stroke-width=".5"/>
    <circle cx="4" cy="2" r="1.2" fill="#999"/><circle cx="136" cy="55" r="1.2" fill="#999"/>
    <polyline fill="none" stroke="var(--navy)" stroke-width=".6" points="15,55 23,36 31,47 47,40 68,55"/>
    <polyline fill="none" stroke="var(--orange)" stroke-width=".6" points="23,55 31,25 47,19 68,43 76,55 90,26 101,36 111,30 120,55"/>
    <g fill="var(--navy)"><circle cx="15" cy="55" r=".9"/><circle cx="23" cy="36" r=".9"/><circle cx="31" cy="47" r=".9"/><circle cx="47" cy="40" r=".9"/><circle cx="68" cy="55" r=".9"/></g>
    <g fill="var(--orange)"><circle cx="23" cy="55" r=".9"/><circle cx="31" cy="25" r=".9"/><circle cx="47" cy="19" r=".9"/><circle cx="68" cy="43" r=".9"/><circle cx="76" cy="55" r=".9"/><circle cx="90" cy="26" r=".9"/><circle cx="101" cy="36" r=".9"/><circle cx="111" cy="30" r=".9"/><circle cx="120" cy="55" r=".9"/></g>
  </svg>
  <div style="position:absolute;left:165px;top:56px;width:96px">
    <div class="orange-t">Title Goes Here</div>
    <p class="mini-copy" style="margin-bottom:6px">Lorem ipsum dolor sit amet, consectetuer adipiscing elit, sed diam nonummy nibh euismod tincidunt ut laoreet dolore magna aliquam erat volutpat. Ut wisi enim ad minim veniam, quis nostrud exerci tation ullamcorper suscipit lobortis nisl ut</p>
    <div class="orange-t">Title Goes Here</div>
    <p class="mini-copy" style="margin-bottom:6px">Lorem ipsum dolor sit amet, consectetuer adipiscing elit, sed diam nonummy nibh euismod tincidunt ut laoreet dolore magna aliquam erat volutpat. Ut wisi enim ad minim veniam, quis nostrud exerci tation ullamcorper suscipit lobortis nisl ut</p>
    <div class="orange-t">Title Goes Here</div>
    <p class="mini-copy">Lorem ipsum dolor sit amet, consectetuer adipiscing elit, sed diam nonummy nibh euismod tincidunt ut laoreet dolore magna aliquam erat volutpat. Ut wisi enim ad minim veniam, quis nostrud exerci tation ullamcorper suscipit lobortis nisl ut</p>
  </div>
  <div class="brand brand-sm">PARTWISE HELM</div>
  <div class="page-no">04</div>
</section>

<!-- Table -->
<section class="slide col-l row4">
  <div class="head-band"><div class="head-title display">HEADING GOES HERE</div></div>
  <table class="data-table">
    <tr><th style="width:76px">Heading Goes Here</th><th class="hl">Heading<br>Goes Here</th><th>Heading<br>Goes Here</th><th>Heading<br>Goes Here</th><th>Heading<br>Goes Here</th></tr>
    <tr><td>Lorem Ipsum Goes Here</td><td>23</td><td>12</td><td>78</td><td>12</td></tr>
    <tr><td>Lorem Ipsum Goes Here</td><td>45</td><td>56</td><td>12</td><td>56</td></tr>
    <tr><td>Lorem Ipsum Goes Here</td><td>78</td><td>76</td><td>34</td><td>76</td></tr>
    <tr><td>Lorem Ipsum Goes Here</td><td>22</td><td>12</td><td>55</td><td>12</td></tr>
    <tr><td>Lorem Ipsum Goes Here</td><td>34</td><td>66</td><td>45</td><td>66</td></tr>
    <tr><td>Lorem Ipsum Goes Here</td><td>67</td><td>47</td><td>78</td><td>47</td></tr>
    <tr><td>Lorem Ipsum Goes Here</td><td>87</td><td>67</td><td>12</td><td>67</td></tr>
  </table>
  <div class="col-frame"></div>
  <div class="brand brand-sm">PARTWISE HELM</div>
  <div class="page-no">05</div>
</section>

<!-- Cards -->
<section class="slide col-r row4">
  <div class="head-band"><div class="head-title display">HEADING GOES HERE</div></div>
  <p style="position:absolute;left:10px;top:50px;width:258px;font-size:3.2px;line-height:1.3">Northvale Minerals Ltd (ASX: NVM) is an Australian exploration company with brownfield metals projects in North America. The Company's strategy is to develop a portfolio of projects that support the green economy through the discovery and delivery of commodities that promote electrification and decarbonisation. We seek to maximise shareholder value through the acquisition, discovery, and advancement of high quality precious, base, and strategic metal projects in North America.</p>
  <div class="card" style="left:14px"><div class="ph" role="img" aria-label="Photo of colleagues working around an office table" style="background:linear-gradient(135deg,#d8dcdd,#6b7076)"></div><div class="orange-t">Heading Goes Here</div><div class="bullet">Lorem ipsum dolar sit amet, consectetur adipising edit. Vivamus eu dui ex.</div></div>
  <div class="card" style="left:102px"><div class="ph" role="img" aria-label="Photo of a hand using a tablet with digital graphics" style="background:linear-gradient(135deg,#bfe0ef,#4d7fa6 60%,#23364f)"></div><div class="orange-t">Heading Goes Here</div><div class="bullet">Lorem ipsum dolar sit amet, consectetur adipising edit. Vivamus eu dui ex.</div></div>
  <div class="card" style="left:190px"><div class="ph" role="img" aria-label="Photo of people reviewing charts on a tablet" style="background:linear-gradient(135deg,#eef1f4,#a9b8c8 60%,#6c88a8)"></div><div class="orange-t">Heading Goes Here</div><div class="bullet">Lorem ipsum dolar sit amet, consectetur adipising edit. Vivamus eu dui ex.</div></div>
  <div class="brand brand-sm">PARTWISE HELM</div>
  <div class="page-no">06</div>
</section>

<!-- Team -->
<section class="slide col-l row5">
  <div class="photo" role="img" aria-label="Dimmed photo of a team meeting behind the heading" style="left:0;top:0;width:277px;height:79px;background:linear-gradient(180deg,#4f5a67,var(--navy))"></div>
  <div class="display" style="position:absolute;left:17px;top:19px;font-size:13px;color:var(--orange)">HEADING GOES HERE</div>
  <div class="person" style="left:26px"><div class="avatar"></div><div class="name">Name Here</div><p class="mini-copy">Lorem ipsum dolor sit amet, consectetuer adipiscing elit, sed diam nonummy nibh euismod tincidunt ut laoreet dolore magna aliquam erat volutpat. Ut wisi enim ad minim veniam, quis nostrud exerci tation</p></div>
  <div class="person" style="left:86px"><div class="avatar"></div><div class="name">Name Here</div><p class="mini-copy">Lorem ipsum dolor sit amet, consectetuer adipiscing elit, sed diam nonummy nibh euismod tincidunt ut laoreet dolore magna aliquam erat volutpat. Ut wisi enim ad minim veniam, quis nostrud exerci tation</p></div>
  <div class="person" style="left:146px"><div class="avatar"></div><div class="name">Name Here</div><p class="mini-copy">Lorem ipsum dolor sit amet, consectetuer adipiscing elit, sed diam nonummy nibh euismod tincidunt ut laoreet dolore magna aliquam erat volutpat. Ut wisi enim ad minim veniam, quis nostrud exerci tation</p></div>
  <div class="person" style="left:206px"><div class="avatar"></div><div class="name">Name Here</div><p class="mini-copy">Lorem ipsum dolor sit amet, consectetuer adipiscing elit, sed diam nonummy nibh euismod tincidunt ut laoreet dolore magna aliquam erat volutpat. Ut wisi enim ad minim veniam, quis nostrud exerci tation</p></div>
  <div class="brand brand-sm">PARTWISE HELM</div>
  <div class="page-no">07</div>
</section>

<!-- Thank you -->
<section class="slide col-r row5 on-dark" style="background:var(--navy)">
  <div class="photo" role="img" aria-label="Photo of a smiling executive presenting in a meeting room" style="left:90px;top:0;width:187px;height:160px;background:linear-gradient(90deg,var(--navy) 0%,#3b4452 35%,var(--photo-dark) 70%,#7a8288 100%)"></div>
  <div class="brand brand-lg on-dark">PARTWISE HELM</div>
  <div class="display" style="position:absolute;left:19px;top:58px;font-size:28px">
    <div style="color:var(--white)">THANK</div><div style="color:var(--orange)">YOU!</div>
  </div>
  <div class="contact">www.partwisehelm.tech<br>+44 7700 900123<br>Mara Quill</div>
  <div class="copyright-bar">©2023 Partwise Helm. All Copyright Reserved</div>
</section>

</body>
</html>
```